Wine Label: Corvinte

The project is to create 3 wine labels. The brand name is "Corvinte"

What we need is to have 3 versions: red wine, white wine and rose.

The wine is for young and modern people, between 21 and 31 years old, so it need to be casual, modern and fun, but at the same time it needs to keep the Premiums of a good European wine.

It is from Italy.

Target Market(s)

Young adults, between 21 and 31 years old. wine lovers

Requirements
Must have
• - Modern colors (Black, silver, red, etc.)
• - Clean label
• - Clear font
• - Style
• - The brand + the type of wine (red, white or rose)
Nice to have
• - A symbol to represent the brand
Should not have
• - Many elements
• - No clear fonts
• - No funny colors

```html
<!DOCTYPE html>
<html lang="en">
<head>
<meta charset="utf-8">
<title>Corvinte Wine Labels</title>
<link rel="stylesheet" href="https://fonts.googleapis.com/css2?family=Josefin+Sans:wght@400;600;700&display=swap">
<style>
  :root {
    --paper: #ffffff;
    --ink: #0a0a0a;
    --label-black: #0b0b0b;
    --white-wine: #cfcfcf;
    --white-wine-deep: #7d7d7d;
    --red-wine: #d3140f;
    --red-wine-deep: #8e0c08;
    --rose-wine: #e316d6;
    --rose-wine-deep: #8f0b86;
    --bottle: #1c1418;
  }
  * { box-sizing: border-box; margin: 0; padding: 0; }
  html, body { width: 1200px; height: 900px; overflow: hidden; }
  body {
    position: relative;
    background: var(--paper);
    font-family: "Josefin Sans", sans-serif;
    color: var(--ink);
  }
  .section-title {
    position: absolute;
    font-weight: 600;
    font-size: 34px;
    letter-spacing: 7px;
    line-height: 1;
    white-space: nowrap;
  }
  .section-title--top { left: 168px; top: 84px; }
  .section-title--main { left: 152px; top: 260px; }
  .section-title--sample { left: 955px; top: 118px; }

  /* variant colours */
  .variant--white { --accent: var(--white-wine); --accent-deep: var(--white-wine-deep); }
  .variant--red   { --accent: var(--red-wine);   --accent-deep: var(--red-wine-deep); }
  .variant--rose  { --accent: var(--rose-wine);  --accent-deep: var(--rose-wine-deep); }

  /* top (neck) label */
  .neck-label {
    position: absolute;
    top: 118px;
    width: 204px;
    height: 128px;
    background: var(--label-black);
    overflow: hidden;
  }
  .neck-label--white { left: 38px; }
  .neck-label--red   { left: 340px; }
  .neck-label--rose  { left: 636px; }
  .neck-label__ornament {
    position: absolute;
    left: 22px; right: 22px; top: 10px; bottom: 10px;
    background: linear-gradient(90deg, var(--accent) 0%, var(--accent-deep) 50%, var(--accent) 100%);
    clip-path: polygon(0 0, 38% 30%, 62% 30%, 100% 0, 100% 100%, 62% 70%, 38% 70%, 0 100%);
  }
  .neck-label__band {
    position: absolute;
    left: 26px; right: 26px; top: 50px; height: 30px;
    background: var(--label-black);
    border-top: 2px solid var(--accent);
    border-bottom: 2px solid var(--accent);
    display: flex; align-items: center; justify-content: center;
  }
  .neck-label__name {
    color: var(--accent);
    font-weight: 600;
    font-size: 22px;
    letter-spacing: 3px;
    line-height: 1;
    padding-top: 3px;
  }

  /* main label */
  .main-label {
    position: absolute;
    top: 300px;
    width: 269px;
    height: 503px;
    background: var(--label-black);
    overflow: hidden;
  }
  .main-label--white { left: 5px; }
  .main-label--red   { left: 307px; }
  .main-label--rose  { left: 603px; }
  .main-label__ornament {
    position: absolute;
    background: radial-gradient(circle at var(--origin), var(--accent) 0%, var(--accent-deep) 85%);
  }
  .main-label__ornament--upper {
    --origin: 0 0;
    left: 23px; top: 18px; width: 225px; height: 210px;
    clip-path: polygon(0 0, 100% 0, 100% 12%, 55% 40%, 28% 100%, 0 100%);
  }
  .main-label__ornament--lower {
    --origin: 100% 100%;
    left: 100px; top: 335px; width: 146px; height: 168px;
    clip-path: polygon(100% 0, 100% 100%, 0 100%, 25% 78%, 62% 48%);
  }
  .main-label__title-block {
    position: absolute;
    left: 23px; right: 23px; top: 258px; height: 78px;
    border-top: 3px solid var(--accent);
    border-bottom: 3px solid var(--accent);
    text-align: center;
  }
  .main-label__name {
    display: block;
    margin-top: 15px;
    color: var(--accent);
    font-weight: 600;
    font-size: 35px;
    letter-spacing: 5px;
    line-height: 1;
  }
  .main-label__type {
    display: block;
    margin-top: 7px;
    color: var(--accent);
    font-family: Arial, Helvetica, sans-serif;
    font-size: 12px;
    letter-spacing: 1.5px;
    line-height: 1;
  }

  /* sample render */
  .sample-render {
    position: absolute;
    left: 905px; top: 212px;
    width: 275px; height: 490px;
    border-radius: 40px 40px 24px 24px;
    background: linear-gradient(90deg, #0e0a0c 0%, var(--bottle) 45%, #3a2a32 60%, #0e0a0c 100%);
  }
</style>
</head>
<body>
  <h2 class="section-title section-title--top">WINE BOTTLE TOP LABEL</h2>
  <h2 class="section-title section-title--main">WINE BOTTLE MAIN LABEL</h2>
  <h2 class="section-title section-title--sample">SAMPLE</h2>

  <section class="neck-label neck-label--white variant--white">
    <div class="neck-label__ornament" role="img" aria-label="Silver floral swirl ornament"></div>
    <div class="neck-label__band"><span class="neck-label__name">CORVINTE</span></div>
  </section>
  <section class="neck-label neck-label--red variant--red">
    <div class="neck-label__ornament" role="img" aria-label="Red floral swirl ornament"></div>
    <div class="neck-label__band"><span class="neck-label__name">CORVINTE</span></div>
  </section>
  <section class="neck-label neck-label--rose variant--rose">
    <div class="neck-label__ornament" role="img" aria-label="Pink floral swirl ornament"></div>
    <div class="neck-label__band"><span class="neck-label__name">CORVINTE</span></div>
  </section>

  <section class="main-label main-label--white variant--white">
    <div class="main-label__ornament main-label__ornament--upper" role="img" aria-label="Silver floral swirl ornament in the upper corner"></div>
    <div class="main-label__title-block">
      <span class="main-label__name">CORVINTE</span>
      <span class="main-label__type">WHITE WINE</span>
    </div>
    <div class="main-label__ornament main-label__ornament--lower" role="img" aria-label="Silver floral swirl ornament in the lower corner"></div>
  </section>
  <section class="main-label main-label--red variant--red">
    <div class="main-label__ornament main-label__ornament--upper" role="img" aria-label="Red floral swirl ornament in the upper corner"></div>
    <div class="main-label__title-block">
      <span class="main-label__name">CORVINTE</span>
      <span class="main-label__type">RED WINE</span>
    </div>
    <div class="main-label__ornament main-label__ornament--lower" role="img" aria-label="Red floral swirl ornament in the lower corner"></div>
  </section>
  <section class="main-label main-label--rose variant--rose">
    <div class="main-label__ornament main-label__ornament--upper" role="img" aria-label="Pink floral swirl ornament in the upper corner"></div>
    <div class="main-label__title-block">
      <span class="main-label__name">CORVINTE</span>
      <span class="main-label__type">ROSE WINE</span>
    </div>
    <div class="main-label__ornament main-label__ornament--lower" role="img" aria-label="Pink floral swirl ornament in the lower corner"></div>
  </section>

  <div class="sample-render" role="img" aria-label="Three dark wine bottles wearing the white, rose and red labels"></div>
</body>
</html>
```